Tech business card design

We need an amazing business card design for our new business 'Brakka' a marketing tech startup based in Sydney, Australia. We provide an online marketplace for businesses to search and buy advertising media, connect with service providers and learn more about marketing. We wish to communicate 'cool tech', reliability and professionalism and design based around our logo.

Target Market(s)

Business Owners

Contact Information for Business Card

Name
Position
Email Address
Website
Phone Number

Font styles to use
Other font styles liked:
• Avenir & Avenir Next

Colors

Designer to choose colors to be used in the design.

```html
<!DOCTYPE html>
<html lang="en">
<head>
<meta charset="utf-8">
<title>Brakka business card</title>
<link rel="stylesheet" href="https://fonts.googleapis.com/css2?family=Nunito+Sans:wght@300;400;700;800&display=swap">
<style>
  :root {
    --navy: #131238;
    --ink: #333333;
    --border: #4a4a4a;
    --paper: #ffffff;
    --green: #3ecf8e;
    --teal: #33bba8;
    --blue: #2aa6d2;
  }
  * { box-sizing: border-box; margin: 0; padding: 0; }
  html, body { width: 1200px; height: 824px; overflow: hidden; background: var(--paper); }
  body { position: relative; font-family: "Nunito Sans", "Avenir Next", sans-serif; color: var(--ink); }

  .card {
    position: absolute; top: 70px; width: 385px; height: 677px;
    border: 1px solid var(--border); background: var(--paper); overflow: hidden;
  }
  .card--front { left: 136px; }
  .card--back { left: 689px; }

  .brand-name { font-weight: 800; color: var(--navy); line-height: 1; }
  .card--front .brand-name {
    position: absolute; left: 34px; top: 36px; font-size: 88px; letter-spacing: -3px;
  }
  .front-bar {
    position: absolute; left: 0; top: 143px; width: 323px; height: 16px; background: var(--navy);
  }
  .front-artwork {
    position: absolute; left: 0; top: 370px; width: 100%; height: 307px;
    background: linear-gradient(120deg, var(--navy) 0%, var(--navy) 38%, var(--blue) 62%, var(--teal) 80%, var(--green) 100%);
  }

  .holder-name {
    position: absolute; left: 30px; top: 102px; font-size: 38px; font-weight: 800;
    color: #151515; letter-spacing: 0.3px;
  }
  .name-rule { position: absolute; left: 0; top: 156px; width: 323px; height: 3px; background: var(--navy); }
  .holder-position { position: absolute; left: 30px; top: 166px; font-size: 26px; font-weight: 300; color: #222; }

  .contact { position: absolute; left: 30px; font-size: 22px; display: flex; align-items: center; gap: 6px; white-space: nowrap; }
  .contact--email { top: 364px; font-weight: 700; }
  .contact--phone { top: 399px; font-weight: 400; }
  .contact--web { top: 612px; font-weight: 700; font-size: 24px; gap: 4px; }
  .icon-box { display: inline-flex; align-items: center; font-weight: 700; }
  .icon-box svg { width: 18px; height: 18px; margin: 0 1px; }

  .card--back .brand-name { position: absolute; left: 29px; top: 562px; font-size: 44px; letter-spacing: -1.5px; }

  .slogan {
    position: absolute; left: 366px; top: 346px; transform: translate(-50%, -50%) rotate(-90deg);
    font-size: 15px; font-weight: 400; letter-spacing: 10px; white-space: nowrap; color: #222;
  }
</style>
</head>
<body>
  <section class="card card--front">
    <div class="brand-name">brakka</div>
    <div class="front-bar"></div>
    <div class="front-artwork" role="img" aria-label="Decorative flowing shapes in navy and a blue-to-green gradient"></div>
  </section>

  <section class="card card--back">
    <h1 class="holder-name">Your name</h1>
    <div class="name-rule"></div>
    <p class="holder-position">Your Position</p>

    <p class="contact contact--email">
      <span class="icon-box">[<svg viewBox="0 0 18 18"><rect x="2" y="4" width="14" height="10" fill="var(--ink)"/><path d="M2.5 4.5 L9 10 L15.5 4.5" stroke="#fff" stroke-width="1.4" fill="none"/></svg>]</span>
      your email@brakka.com
    </p>
    <p class="contact contact--phone">
      <span class="icon-box">[<svg viewBox="0 0 18 18"><path fill="var(--ink)" d="M4 2 L7 2 L8 6 L6 7.5 C7 10 8 11 10.5 12 L12 10 L16 11 L16 14 C16 15 15 16 14 16 C8 15.5 2.5 10 2 4 C2 3 3 2 4 2 Z"/></svg>]</span>
      + 00 000 0000
    </p>

    <div class="brand-name">brakka</div>

    <p class="contact contact--web">
      <span class="icon-box">[<svg viewBox="0 0 18 18" fill="none" stroke="var(--ink)" stroke-width="1.3"><circle cx="9" cy="9" r="7"/><ellipse cx="9" cy="9" rx="3" ry="7"/><path d="M2 9 H16 M3 5.5 H15 M3 12.5 H15"/></svg>]</span>
      http://yourwebsite.com
    </p>

    <p class="slogan">PUT YOUR SLOGAN HERE YOUR SLOGAN</p>
  </section>
</body>
</html>
```